Business Card Design Project

Business Card
We are rebranding with a new logo
Industry/Entity Type
Business
Contact Information for Business Card
Doug Fenwick +61 427581962 doug@kova.com.au P.O. Box 287 Millcrest QLD 4519
Requirements
Must have
- Logo

```html
<!DOCTYPE html>
<html lang="en">
<head>
<meta charset="utf-8">
<title>Kova Global – Business Card</title>
<link href="https://fonts.googleapis.com/css2?family=Open+Sans:wght@400;600;700&display=swap" rel="stylesheet">
<style>
  :root {
    --canvas: #e4e6ea;
    --card: #ffffff;
    --navy: #134a6e;
    --deep-blue: #0b5f8f;
    --bright-blue: #0a8fc9;
    --orange: #f28a2e;
    --text-dark: #1d3557;
  }
  * { margin: 0; padding: 0; box-sizing: border-box; }
  html, body {
    width: 1200px; height: 900px; overflow: hidden;
    background: var(--canvas);
    font-family: "Open Sans", sans-serif;
  }
  .stage {
    width: 1200px; height: 900px;
    display: flex; flex-direction: column; align-items: center; justify-content: center;
    gap: 40px;
  }
  .card {
    position: relative;
    width: 700px; height: 400px;
    background: var(--card);
    border-radius: 20px;
    overflow: hidden;
    box-shadow: 0 6px 18px rgba(0,0,0,0.12);
  }
  .card-back { display: flex; align-items: center; justify-content: center; }
  .brand {
    display: flex; align-items: center; gap: 12px;
    color: var(--bright-blue);
    font-weight: 700;
    letter-spacing: 4px;
    text-transform: uppercase;
  }
  .brand-dot { border-radius: 50%; background: var(--orange); flex: none; }
  .card-back .brand { font-size: 40px; }
  .card-back .brand-dot { width: 30px; height: 30px; }

  .header-band {
    position: absolute; left: 0; top: 0;
    width: 700px; height: 140px;
    background: linear-gradient(90deg, var(--orange) 0%, var(--bright-blue) 45%, var(--deep-blue) 100%);
  }
  .card-front .brand {
    position: absolute; right: 50px; top: 196px; font-size: 30px;
  }
  .card-front .brand-dot { width: 22px; height: 22px; }
  .holder { position: absolute; left: 40px; top: 198px; }
  .holder-name { font-size: 26px; font-weight: 700; color: var(--text-dark); line-height: 1.1; }
  .holder-role { font-size: 17px; color: var(--orange); margin-top: 2px; }
  .divider {
    position: absolute; left: 40px; right: 40px; top: 268px;
    height: 1.5px; background: var(--navy);
  }
  .contacts {
    position: absolute; right: 42px; top: 278px;
    list-style: none; text-align: right;
  }
  .contacts li {
    display: flex; align-items: center; justify-content: flex-end; gap: 10px;
    font-size: 15px; color: var(--text-dark); line-height: 17px; height: 18px;
  }
  .contacts svg { width: 15px; height: 15px; flex: none; }
  .services {
    position: absolute; left: 32px; top: 352px;
    width: 520px; height: 30px;
    background: var(--bright-blue);
    color: #fff; font-size: 14px; font-weight: 600;
    letter-spacing: 0.5px;
    display: flex; align-items: center; padding-left: 16px;
    text-transform: uppercase;
  }
</style>
</head>
<body>
<main class="stage">
  <section class="card card-back" aria-label="Business card back">
    <div class="brand"><span class="brand-dot"></span>Kova Global</div>
  </section>

  <section class="card card-front" aria-label="Business card front">
    <div class="header-band" role="img" aria-label="Decorative header in orange and blue brand tones"></div>

    <div class="holder">
      <p class="holder-name">Doug Fenwick</p>
      <p class="holder-role">Managing Director</p>
    </div>

    <div class="brand"><span class="brand-dot"></span>Kova Global</div>

    <div class="divider"></div>

    <ul class="contacts">
      <li>+61 427581962
        <svg viewBox="0 0 16 16"><path d="M3 1h3l1.5 4-2 1.2a9 9 0 0 0 4.3 4.3l1.2-2 4 1.5v3c0 1-1 2-2 2C6.5 15 1 9.5 1 3c0-1 1-2 2-2z" fill="#0a8fc9"/></svg>
      </li>
      <li>doug@kova.com.au
        <svg viewBox="0 0 16 16"><rect x="1" y="3" width="14" height="10" rx="1" fill="#0a8fc9"/><path d="M1.5 3.5 8 9l6.5-5.5" stroke="#fff" stroke-width="1.3" fill="none"/></svg>
      </li>
      <li>P.O. Box 287 Millcrest QLD 4519
        <svg viewBox="0 0 16 16"><path d="M8 1 1 7.5h2V15h4v-4h2v4h4V7.5h2z" fill="#0a8fc9"/></svg>
      </li>
      <li>kova.com.au
        <svg viewBox="0 0 16 16"><circle cx="8" cy="8" r="7" fill="#0a8fc9"/><path d="M1 8h14M8 1c-3 3.5-3 10.5 0 14M8 1c3 3.5 3 10.5 0 14" stroke="#fff" stroke-width="1" fill="none"/></svg>
      </li>
    </ul>

    <div class="services">Film Service • Tour Management • Drivers</div>
  </section>
</main>
</body>
</html>
```